Emergency Vehicle Installer and Security Firm Needs a Business Card

Our company "Corvalt" need a business card for our Emergency Vehicle Equipment Installation and Infrastructure Security Business. We are contract designers, manufacturers and installers for Emergency Vehicle Fleets. This includes installation of Emergency Lights, Sirens, Vehicle Graphics and Radio Communications. We also supply this products to an international market. We also do consultant, and installation of high level security access, alarm and surveillance equipment for medium to large size businesses.

The design should represent a level of trust in our professionalism and expertise. It should visually display our ongoing relationship with the emergency services, but not overtake our commitment to high level security options.

Target Market(s)

Emergency Services and Businesses requiring high level security

Industry/Entity Type

Business

Contact Information for Business Card

*note complete details will be given to the winning designer for revising. The name "Mark Pell will be used to fill in name".

Mark Pell
Managing Director
Corvalt NZ Limited
Phone: +64 027 604 91352
Email: mark.pell@corvalt-example.co.nz

Requirements
Must have
• Card must be in black. Using our logo on the top as supplied. Designers should try having the reverse side as a blurred image of police lights (red and blue) with our logo in greyscale in the centre (this is not particularly a requirement, but feel free to play around with this option).
Nice to have
• A card design that looks good when spot UV printed. A clean compact and graphic design. A grey scale feel on the front (excluding logo, but you can play around with that idea). Rounded smooth text.
Should not have
• Will update this section as designs come through - feel free to submit what you feel would look good.

```html
<!DOCTYPE html>
<html lang="en">
<head>
<meta charset="UTF-8">
<title>Corvalt Business Card</title>
<link href="https://fonts.googleapis.com/css2?family=Jost:wght@400;600&display=swap" rel="stylesheet">
<style>
  :root {
    --stage: #6b6b6b;
    --stage-light: #7d7d7d;
    --card-black: #0b0b0b;
    --card-black-soft: #1a1a1a;
    --brand-red: #e41f28;
    --brand-red-light: #f2353c;
    --text-white: #ffffff;
    --text-dark: #1a1a1a;
  }
  * { margin: 0; padding: 0; box-sizing: border-box; }
  html, body {
    width: 1200px;
    height: 950px;
    overflow: hidden;
  }
  body {
    background: radial-gradient(ellipse at center, var(--stage-light) 0%, var(--stage) 75%);
    font-family: "Jost", sans-serif;
    position: relative;
  }
  .card {
    position: absolute;
    width: 620px;
    height: 354px;
    border-radius: 26px;
    background: linear-gradient(160deg, var(--card-black-soft) 0%, var(--card-black) 55%);
    overflow: hidden;
    box-shadow: 0 18px 40px rgba(0, 0, 0, 0.35);
  }
  .card--front { left: 120px; top: 90px; }
  .card--back { left: 460px; top: 500px; }

  .brand {
    position: absolute;
    left: 0; right: 0; top: 50%;
    transform: translateY(-50%);
    display: flex;
    align-items: center;
    justify-content: center;
    gap: 16px;
  }
  .brand__mark {
    width: 22px;
    height: 22px;
    border-radius: 50%;
    background: var(--brand-red);
  }
  .brand__name {
    font-weight: 600;
    font-size: 58px;
    letter-spacing: 1px;
    color: var(--text-white);
    line-height: 1;
  }

  .contact-band {
    position: absolute;
    left: 40%;
    right: 0;
    top: 22%;
    height: 50%;
    background: linear-gradient(135deg, var(--brand-red) 0%, var(--brand-red-light) 100%);
  }
  .contact {
    position: absolute;
    left: 46%;
    top: 27%;
    color: var(--text-white);
    line-height: 1.25;
  }
  .contact__name {
    font-size: 24px;
    font-weight: 400;
    letter-spacing: 1px;
    color: var(--text-dark);
    text-transform: uppercase;
  }
  .contact__role {
    font-size: 18px;
    margin-bottom: 10px;
  }
  .contact__line {
    font-size: 16px;
  }
</style>
</head>
<body>
  <section class="card card--front" aria-label="Card front">
    <div class="brand">
      <span class="brand__mark"></span>
      <span class="brand__name">Corvalt</span>
    </div>
  </section>

  <section class="card card--back" aria-label="Card back">
    <div class="contact-band"></div>
    <div class="contact">
      <p class="contact__name">Mark Pell</p>
      <p class="contact__role">Managing Director</p>
      <p class="contact__line">Corvalt NZ Limited</p>
      <p class="contact__line">+64 027 604 91352</p>
      <p class="contact__line">mark.pell@corvalt-example.co.nz</p>
    </div>
  </section>
</body>
</html>
```